Company Website

We need an interactive website designed that for new company. Our company is in the Automotive fleet maintenance business. We have wide ranging customers in many industries e.g Aviation industry, construction industry, transportation etc.
We would like the website to have login accounts where customers can register, login and access their service history. Also we would like to have an appointment system where customers could schedule appointments, once appointments are made that time would no longer be available to be selected as it would be booked etc.

The website should also be updatable and provide areas for showcasing
Our services
Products/parts (possibly store front)
Customer feedback
Appointments
Our customers (where our customers can advertise or be showcased)
About us
Contacts
gallery

We would like designs that have a modern, corporate feel, One that is user friendly.
prefer a design that does not look like a template.

Target Market(s)

Medium to large companies, small business owners and the general motoring public.

Industry/Entity Type

Construction

Requirements
Must have
• Customer login set up so a database of customer vehicle maintenance history as well as the ability to schedule repairs via their account. They could also check the status of a repair.
Nice to have
• Photo gallery to show case current projects.
Our customers page where we can show case our clients they could also post their events on there, promotions etc.

The theme Should be something that's reflective of our core business; fleet maintenance. It would be nice to capture some sort of background in there that depicts some of that for example mixer trucks, tractors,loaders excavators forklifts cars trucks. That's what we deal with. It's up to the designer to capture the Essence of this as much as possible. Impress me.
Should not have
• Would prefer a custom website not a template.

```html
<!DOCTYPE html>
<html lang="en">
<head>
<meta charset="utf-8">
<title>Meridian Fleet &amp; Auto Maintenance</title>
<link href="https://fonts.googleapis.com/css2?family=Open+Sans:wght@400;600;700&display=swap" rel="stylesheet">
<style>
:root{
  --red:#c62026;
  --red-dark:#a8161b;
  --red-light:#d9363b;
  --ink:#333;
  --body:#4a4a4a;
  --muted:#777;
  --hero-bg:#f4f4f4;
  --panel:#f1f1f1;
  --rule:#dcdcdc;
  --footer:#2c2c2c;
  --footer-text:#b9b9b9;
  --active:#3a3a3a;
}
*{margin:0;padding:0;box-sizing:border-box}
html,body{width:1015px;height:1200px;overflow:hidden;background:#fff}
body{font-family:"Open Sans",Arial,sans-serif;color:var(--body);position:relative}
.abs{position:absolute}

/* header */
.brand{left:86px;top:28px;display:flex;align-items:center;gap:8px}
.brand-mark{width:14px;height:14px;background:var(--red)}
.brand-name{font-size:22px;font-weight:700;color:var(--red);letter-spacing:.5px;line-height:1}
.brand-tag{left:108px;top:56px;font-size:10px;font-weight:700;color:var(--red);letter-spacing:.3px}
.fleet-banner{left:371px;top:26px;width:366px;height:62px;border-radius:4px;background:linear-gradient(180deg,#f4f4f4,#d9d9d9)}
.account{right:84px;top:24px;font-size:11.5px;color:var(--ink)}
.account .sep{color:#bbb;margin:0 6px}
.account .login{color:var(--red)}
.search{left:753px;top:52px;width:178px;height:30px;border:1px solid #cfcfcf;font-size:11.5px;color:#888;padding:7px 12px}
.search svg{position:absolute;right:8px;top:7px}

/* nav */
.nav{left:0;top:106px;width:1015px;height:44px;background:linear-gradient(180deg,var(--red-light),var(--red-dark))}
.nav ul{list-style:none;display:flex;position:absolute;left:84px;top:0;height:44px;border-left:1px solid #9e1418}
.nav li{height:44px;line-height:44px;padding:0 15.5px;color:#fff;font-size:12.5px;border-right:1px solid #9e1418;white-space:nowrap}
.nav li.active{background:var(--active)}

/* hero */
.hero{left:0;top:150px;width:1015px;height:346px;background:var(--hero-bg);border-bottom:1px solid #e4e4e4;overflow:hidden}
.hero-photo{left:400px;top:62px;width:598px;height:284px;background:radial-gradient(ellipse at 55% 50%,#ffffff 0%,#e8e8e8 55%,#f4f4f4 100%);z-index:0}
.hero-title{left:102px;top:70px;font-size:25px;line-height:33px;color:var(--ink);font-weight:400;z-index:1;white-space:nowrap}
.hero-text{left:102px;top:140px;width:280px;font-size:11.2px;line-height:19.4px;z-index:1}
.hero-btn{left:102px;top:211px;width:84px;height:32px;background:#555;border-radius:2px;color:#fff;font-size:11.5px;line-height:32px;text-align:center;z-index:1}
.dots{left:102px;top:312px;display:flex;gap:9px;z-index:1}
.dots span{width:12px;height:12px;border-radius:50%;background:#c4c4c4}
.dots span.on{background:#6a6a6a}

/* content */
.about{left:86px;top:525px;width:588px}
.about-title{font-size:23px;font-weight:600;color:#444;line-height:30px;margin-bottom:9px;white-space:nowrap}
.about-title b{color:var(--red);font-weight:700}
.about-photo{float:right;width:234px;height:122px;margin:4px 0 10px 16px;background:linear-gradient(180deg,#b9bdb8 0%,#8c8a6e 45%,#3f4046 100%)}
.about p{font-size:11.2px;line-height:19.4px;margin-bottom:9px}
.about-lead{margin-bottom:14px !important}
.about-body{clear:both;text-align:justify}

/* sidebar */
.side-head{left:698px;width:233px;height:36px;background:linear-gradient(180deg,var(--red-light),var(--red-dark));color:#fff;font-size:14.5px;font-weight:700;line-height:36px;padding-left:14px;border-radius:2px 2px 0 0}
.side-list{left:698px;top:567px;width:233px;height:289px;background:var(--panel);list-style:none;padding-top:13px}
.side-list li{height:30px;font-size:13.5px;color:var(--ink);padding-left:16px}
.side-list li::before{content:"»";margin-right:8px}
.book{left:698px;top:902px;width:233px;height:37px;background:linear-gradient(180deg,var(--red-light),var(--red-dark));color:#fff;font-size:14.5px;font-weight:700;line-height:37px;text-align:center;border-radius:3px;box-shadow:0 1px 2px rgba(0,0,0,.35)}

/* contact strip */
.rule{left:86px;top:986px;width:845px;height:1px;background:var(--rule)}
.contact{top:1010px;display:flex;align-items:center;gap:12px;font-size:11.2px;line-height:19px;color:var(--muted);white-space:nowrap}

/* footer */
.footer{left:0;top:1070px;width:1015px;height:130px;background:var(--footer)}
.foot-links{left:0;top:20px;width:1015px;text-align:center;font-size:12px;color:var(--footer-text)}
.foot-links span.sep{margin:0 10px}
.copy{left:0;top:52px;width:1015px;text-align:center;font-size:11.5px;color:var(--footer-text)}
.social{left:452px;top:86px;display:flex;gap:8px}
.social span{width:22px;height:22px;border-radius:50%;background:#6a6a6a}
</style>
</head>
<body>

<header>
  <div class="abs brand"><span class="brand-mark"></span><span class="brand-name">MERIDIAN</span></div>
  <div class="abs brand-tag">FLEET &amp; AUTO MAINTENANCE</div>
  <div class="abs fleet-banner" role="img" aria-label="Row of fleet vehicles: trucks, a van and a car"></div>
  <div class="abs account">REGISTER<span class="sep">/</span><span class="login">LOGIN</span></div>
  <div class="abs search">Search
    <svg width="14" height="14" viewBox="0 0 14 14"><circle cx="5.5" cy="5.5" r="4" fill="none" stroke="#222" stroke-width="2"/><line x1="8.5" y1="8.5" x2="13" y2="13" stroke="#222" stroke-width="2.4"/></svg>
  </div>
</header>

<nav class="abs nav">
  <ul>
    <li>HOME</li><li>OUR SERVICES</li><li>PRODUCTS</li><li>FEEDBACK</li><li>APPOINTMENTS</li><li>CUSTOMERS</li><li class="active">ABOUT US</li><li>CONTACTS</li><li>GALLERY</li>
  </ul>
</nav>

<section class="abs hero">
  <div class="abs hero-photo" role="img" aria-label="Silver sedan with front door open"></div>
  <h1 class="abs hero-title">Pellentesque habitant<br>morbi tristique</h1>
  <p class="abs hero-text">Curabitur sed velit id enim scelerisque porttitor. Pellentesque id rhoncus lorem. Nullam gravida nisl sit amet massa viverra placerat.</p>
  <div class="abs hero-btn">VIEW MORE</div>
  <div class="abs dots"><span class="on"></span><span></span><span></span><span></span></div>
</section>

<main>
  <div class="abs about">
    <h2 class="about-title"><b>ABOUT</b> Meridian Fleet &amp; Auto Maintenance</h2>
    <div class="about-photo" role="img" aria-label="Truck and cars on a highway"></div>
    <p class="about-lead">Nam tristique, purus ut molestie cursus, est sem luctus diam, at sollicitudin neque lacus vel enim. Integer at odio tellus. Integer auctor mauris urna, non vestibulum quam mollis vel. Phasellus eu adipiscing velit. Cras mollis convallis felis vel vulputate. Etiam mollis imperdiet rutrum. Fusce tellus nibh, vestibulum in ante id, tempor convallis lacus. Curabitur et tellus non diam tincidunt fermentum. Nullam id consectetur urna.</p>
    <div class="about-body">
      <p>Nulla sem tellus, viverra eget ipsum ac, hendrerit ullamcorper leo. Nulla vehicula magna ac nunc luctus, sit amet aliquam odio egestas. Aenean luctus eros eget aliquam semper. Ut dignissim suscipit purus, ac interdum ipsum lacinia id. Praesent quis quam et massa dapibus malesuada. Sed elit lacus, porta in aliquam ac, elementum sed urna. Aenean laoreet massa sit amet massa facilisis dapibus. Fusce ultrices risus est. In ullamcorper malesuada felis. Integer vitae metus cursus, vulputate odio sed, congue ante. Maecenas vestibulum pulvinar libero, eget dapibus diam interdum quis. Donec bibendum sit amet turpis vitae laoreet. Quisque nec erat semper, ultricies ipsum at, malesuada nisl. Pellentesque sagittis felis id venenatis rhoncus. Pellentesque habitant morbi tristique senectus et netus et malesuada fames ac turpis egestas. Suspendisse potenti.</p>
      <p>Quisque enim nisl, semper sit amet lectus nec, fermentum malesuada orci. Aliquam ac risus a nibh eleifend ultricies. Fusce mi mi, porttitor id consequat ut, faucibus ut neque. Fusce nisl mauris, laoreet sed ligula vel, interdum aliquam lectus. Praesent et facilisis mi. Quisque adipiscing augue ligula, non pretium dolor sodales eget. Pellentesque vulputate pharetra lectus vestibulum feugiat. Integer at egestas ligula.</p>
    </div>
  </div>

  <aside>
    <div class="abs side-head" style="top:531px">OUR SERVICES</div>
    <ul class="abs side-list">
      <li>Aviation industry</li><li>Construction industry</li><li>Transportation</li><li>Mixer truck</li><li>Tractors</li><li>Loaders Excavators</li><li>Forklifts</li><li>Trucks</li><li>Cars</li>
    </ul>
    <div class="abs side-head" style="top:862px;border-radius:2px">OUR PROJECTS</div>
    <div class="abs book">BOOK AN APPOINTMENT</div>
  </aside>

  <div class="abs rule"></div>
  <div class="abs contact" style="left:92px">
    <svg width="20" height="24" viewBox="0 0 20 24"><rect x="1" y="1" width="18" height="22" fill="none" stroke="#999" stroke-width="2"/><path d="M7 4v9l3-2 3 2V4" fill="#999"/></svg>
    <div>55, Building name, streetname<br>City - Zip code</div>
  </div>
  <div class="abs contact" style="left:318px">
    <svg width="24" height="26" viewBox="0 0 24 26"><path d="M3 3c3-2 5 0 6 3l-2 3c1 3 4 7 7 9l3-2c3 1 5 3 3 6-2 3-6 2-10-2S1 10 1 7c0-2 1-3 2-4z" fill="#999"/></svg>
    <div>Phone: 555 010 2468</div>
  </div>
  <div class="abs contact" style="left:533px">
    <svg width="26" height="24" viewBox="0 0 26 24"><rect x="1" y="6" width="24" height="17" fill="#999"/><rect x="7" y="1" width="12" height="9" fill="#bbb"/><rect x="12" y="12" width="10" height="8" fill="#ddd"/></svg>
    <div>Fax : 555 010 1357</div>
  </div>
  <div class="abs contact" style="left:726px">
    <svg width="24" height="18" viewBox="0 0 24 18"><rect x="1" y="1" width="22" height="16" fill="#aaa"/><path d="M1 1l11 9 11-9" fill="none" stroke="#eee" stroke-width="1.5"/></svg>
    <div>E-mail : info@meridianfleet.com</div>
  </div>
</main>

<footer class="abs footer">
  <div class="abs foot-links">Home<span class="sep">|</span>Our services<span class="sep">|</span>Products<span class="sep">|</span>Feedback<span class="sep">|</span>Appointments<span class="sep">|</span>Customers<span class="sep">|</span>About us<span class="sep">|</span>Contact us<span class="sep">|</span>Gallery</div>
  <div class="abs copy">Copyright &copy; 2013 &nbsp;Meridian fleet maintenance. &nbsp;All rights reserved.</div>
  <div class="abs social"><span></span><span></span><span></span><span></span></div>
</footer>

</body>
</html>
```